New Label Design Project - Quillfen Dermal

Label Design Brief - Quillfen Dermal
Label Panel Dimensions 1.25" W x 2.375" H (front/back panel)
Hello - our company develops novel products for the skin, & hair care industry as well as dietary supplements. We're looking for a label design for a new product. The product is a premium Topical hair loss/growth serum. I attached the brand logo & 2 other sister products along with some competitive products.
The product is a topical natural hair loss serum for men & women to regrow new hair and help restore hair loss & thinning hair due to vitamin deficiencies, hormone imbalance & aging. It is a science based efficacious serum with a century’s old medicinal herbal formula.
Attached is our logo & some files of other competition. The label must have an upscale, technology flair to it. The product is clinically effective, leveraged by Ancient Wisdom and Modern Science.
Below are attached files of 2 of our products & other generic competition for your perusal.

https://www.shopvarlo.example/item/K7R2TQ4MPL?ref=lst_featured

https://www.shopvarlo.example/item/K7R3ZN8WDH/ref=lst-redir?pg=1&ref=lst_lowprice

Target Market(s)

men & women age 18-80

Requirements
Must have
• see brief
Should not have
• Please do not have a picture of a man or a women on the label.

```html
<!DOCTYPE html>
<html lang="en">
<head>
<meta charset="utf-8">
<title>Quillfen Dermal – Growth Activator DHT Blocker Label</title>
<link rel="stylesheet" href="https://fonts.googleapis.com/css2?family=Montserrat:wght@500;600;700;800;900&display=swap">
<style>
  :root {
    --white: #ffffff;
    --ink: #0b0909;
    --brown-dark: #4a1d12;
    --brown-mid: #8a4a26;
    --copper: #c78540;
    --gold-light: #e9cf9f;
    --gold: #b8894f;
    --gold-dark: #7a5128;
    --night: #140d0e;
    --text-brown: #5a1f16;
    --placeholder-grey: #ececec;
  }
  * { margin: 0; padding: 0; box-sizing: border-box; }
  html, body { width: 809px; height: 1200px; overflow: hidden; background: var(--white); }
  body { font-family: "Montserrat", sans-serif; }

  .label { position: relative; width: 809px; height: 1200px; background: var(--white); overflow: hidden; }

  .edge-bar {
    position: absolute; left: 0; width: 100%; height: 10px;
    background: linear-gradient(90deg, var(--brown-dark) 0%, var(--brown-mid) 30%, var(--gold-light) 48%, var(--brown-mid) 60%, #3a0f0c 100%);
  }
  .edge-bar--top { top: 0; }
  .edge-bar--bottom { bottom: 0; background: linear-gradient(90deg, #3a0f0c 0%, var(--brown-dark) 40%, var(--copper) 60%, var(--brown-mid) 100%); }

  .hex-backdrop {
    position: absolute; left: 0; width: 100%;
    background: linear-gradient(180deg, #ffffff 0%, #f6f6f6 50%, #ffffff 100%);
  }
  .hex-backdrop--top { top: 10px; height: 276px; }
  .hex-backdrop--mid { top: 759px; height: 209px; }
  .hex-backdrop--bottom { top: 1029px; height: 161px; }

  .brand {
    position: absolute; top: 172px; left: 0; width: 100%;
    display: flex; justify-content: center; align-items: center; gap: 16px;
  }
  .brand__dot { width: 22px; height: 22px; border-radius: 50%; background: var(--brown-mid); }
  .brand__name { font-weight: 600; font-size: 46px; line-height: 56px; color: var(--text-brown); letter-spacing: 1px; }

  .band-growth {
    position: absolute; top: 286px; left: 0; width: 100%; height: 192px;
    background: linear-gradient(90deg, #4e1c12 0%, #8a4a26 25%, #c98a45 50%, #9a5a2c 75%, #7a3c1f 100%);
    display: flex; flex-direction: column; justify-content: center; align-items: center;
  }
  .band-growth__line { color: var(--white); font-weight: 800; font-size: 90px; line-height: 92px; letter-spacing: 0; }

  .band-dht {
    position: absolute; top: 478px; left: 0; width: 100%; height: 281px;
    background: radial-gradient(ellipse at 55% 45%, #2a1a1a 0%, var(--night) 70%);
    text-align: center;
  }
  .band-dht__big {
    display: block; margin-top: 6px;
    font-weight: 900; font-size: 198px; line-height: 172px; letter-spacing: -4px;
    background: linear-gradient(90deg, var(--gold-dark) 0%, var(--gold) 30%, var(--gold-light) 70%, #c9a575 100%);
    -webkit-background-clip: text; background-clip: text; color: transparent;
  }
  .band-dht__sub { display: block; margin-top: 0; color: var(--white); font-weight: 800; font-size: 86px; line-height: 90px; }

  .molecule {
    position: absolute; top: 770px; left: 240px; width: 330px; height: 185px;
    background: linear-gradient(135deg, #d9d9d9 0%, #bfbfbf 100%);
  }

  .audience-bar {
    position: absolute; top: 968px; left: 0; width: 100%; height: 61px;
    background: var(--ink); color: var(--white);
    display: flex; justify-content: center; align-items: center;
    font-weight: 600; font-size: 31px; letter-spacing: 3px;
  }

  .claims { position: absolute; top: 1060px; left: 105px; list-style: none; }
  .claims__item {
    display: flex; align-items: center; gap: 6px;
    color: var(--text-brown); font-weight: 700; font-size: 24px; line-height: 36px;
  }
  .claims__tick { width: 15px; height: 15px; }

  .mortar {
    position: absolute; top: 1045px; left: 514px; width: 160px; height: 110px;
    background: linear-gradient(180deg, var(--placeholder-grey) 0%, #d6d6d6 100%);
  }

  .volume {
    position: absolute; top: 1145px; left: 348px; width: 112px; height: 45px;
    background: linear-gradient(90deg, var(--brown-dark), var(--brown-mid));
    color: var(--white); font-weight: 700; font-size: 28px;
    display: flex; justify-content: center; align-items: center;
  }
</style>
</head>
<body>
<main class="label">
  <div class="edge-bar edge-bar--top"></div>

  <div class="hex-backdrop hex-backdrop--top" role="img" aria-label="Faint hexagonal molecular grid pattern"></div>
  <div class="hex-backdrop hex-backdrop--mid" role="img" aria-label="Faint hexagonal molecular grid pattern"></div>
  <div class="hex-backdrop hex-backdrop--bottom" role="img" aria-label="Faint hexagonal molecular grid pattern"></div>

  <div class="brand">
    <span class="brand__dot"></span>
    <span class="brand__name">Quillfen Dermal</span>
  </div>

  <section class="band-growth">
    <span class="band-growth__line">GROWTH</span>
    <span class="band-growth__line">ACTIVATOR</span>
  </section>

  <section class="band-dht" role="img" aria-label="Dark flowing hair-line texture behind product name">
    <span class="band-dht__big">DHT</span>
    <span class="band-dht__sub">BLOCKER</span>
  </section>

  <div class="molecule" role="img" aria-label="Ball-and-stick steroid molecule illustration"></div>

  <div class="audience-bar">FOR MEN AND WOMEN</div>

  <ul class="claims">
    <li class="claims__item">
      <svg class="claims__tick" viewBox="0 0 16 16" aria-hidden="true"><circle cx="8" cy="8" r="6.5" fill="none" stroke="#5a1f16" stroke-width="1.8"/><path d="M4.8 8.2l2.2 2.2 4.2-4.6" fill="none" stroke="#5a1f16" stroke-width="1.8"/></svg>
      PARABEN FREE
    </li>
    <li class="claims__item">
      <svg class="claims__tick" viewBox="0 0 16 16" aria-hidden="true"><circle cx="8" cy="8" r="6.5" fill="none" stroke="#5a1f16" stroke-width="1.8"/><path d="M4.8 8.2l2.2 2.2 4.2-4.6" fill="none" stroke="#5a1f16" stroke-width="1.8"/></svg>
      TIME -RELEASED
    </li>
  </ul>

  <div class="mortar" role="img" aria-label="Sketched mortar and pestle illustration"></div>

  <div class="volume">2fl.oz</div>

  <div class="edge-bar edge-bar--bottom"></div>
</main>
</body>
</html>
```